Sign Advertisment for Condominium Development

I need a sign created that will be placed in front of a building that is being converted into a luxury condominium development.

The sign needs to say:

Two, Boutique Luxury Condominiums Delivering late 2015.

Luxury Finishes // Designer Kitchens and Bath // Each Unit over 2,000 Square Feet

Deeded Parking Included with Each Unit

To Learn More, Contact:

Marissa Talbot or Vernon Pike
(202) 555-0147
Marissa.Talbot@example-realty.com

I need a small disclaimer at the bottom stating:

These Condominium(s) have not been registered by the Office of Residential Standards and Property Oversight Bureau Tenancy Transition and Transfer Section. A Condominium Unit may be reserved on a non-binding reservation agreement, but no contract of sale or lease that is binding on the purchaser may be entered into prior to registration.

Target Market(s)

Young professionals seeking luxury condominium

Industry/Entity Type

Building

Font styles to use
Serif

Colors
00a88f
ffffff

```html
<!DOCTYPE html>
<html lang="en">
<head>
<meta charset="utf-8">
<title>Boutique Luxury Condominiums – Sign</title>
<link rel="stylesheet" href="https://fonts.googleapis.com/css2?family=Lato:wght@300;400;700&display=swap">
<style>
  :root {
    --ink: #0c0c0c;
    --ink-soft: #1c1c1c;
    --gold: #a58c5f;
    --gold-light: #8f7b57;
    --white: #ffffff;
    --rule: #8c7853;
    --fine-print: #2a2a2a;
  }
  html, body {
    margin: 0;
    padding: 0;
    width: 795px;
    height: 1200px;
    overflow: hidden;
    background: var(--ink);
  }
  .sign {
    position: relative;
    width: 795px;
    height: 1200px;
    font-family: "Lato", sans-serif;
    text-align: center;
    text-transform: uppercase;
    color: var(--gold);
  }
  .blueprint-backdrop {
    position: absolute;
    inset: 0;
    background:
      radial-gradient(ellipse at 50% 30%, #202020 0%, #141414 45%, var(--ink) 100%);
  }
  .line {
    position: absolute;
    left: 0;
    right: 0;
    margin: 0;
    line-height: 1;
    white-space: nowrap;
  }
  .headline-top   { top: 222px; font-size: 45px; font-weight: 300; color: var(--gold-light); }
  .headline-top strong { font-weight: 700; color: var(--gold); }
  .headline-main  { top: 260px; font-size: 53px; font-weight: 700; color: var(--white); }
  .headline-date  { top: 322px; font-size: 45px; font-weight: 300; color: var(--gold-light); }

  .rule {
    position: absolute;
    left: 84px;
    width: 626px;
    height: 3px;
    background: var(--rule);
  }
  .rule-top    { top: 519px; }
  .rule-bottom { top: 666px; }

  .feature { font-size: 31px; font-weight: 300; color: var(--gold-light); }
  .feature-1 { top: 540px; }
  .feature-2 { top: 579px; }
  .feature-3 { top: 618px; }

  .parking-lead { top: 731px; font-size: 29px; font-weight: 300; color: var(--white); }
  .parking-note { top: 768px; font-size: 29px; font-weight: 700; color: var(--white); }

  .contact-tag {
    position: absolute;
    top: 877px;
    left: 184px;
    width: 448px;
    height: 35px;
    background: var(--gold);
    color: var(--white);
    font-size: 26px;
    font-weight: 400;
    line-height: 35px;
  }
  .contact { font-size: 26px; font-weight: 400; color: var(--gold); }
  .contact-names { top: 924px; }
  .contact-phone { top: 957px; }
  .contact-email { top: 988px; }

  .disclaimer {
    position: absolute;
    top: 1080px;
    left: 44px;
    right: 44px;
    margin: 0;
    font-size: 13px;
    line-height: 17px;
    text-transform: none;
    text-align: justify;
    text-align-last: center;
    color: var(--fine-print);
    font-weight: 400;
  }
</style>
</head>
<body>
  <main class="sign">
    <div class="blueprint-backdrop" role="img" aria-label="Faint architectural floor-plan drawing in dark grey lines covering the background"></div>

    <h1 class="line headline-top">Two, <strong>Boutique Luxury</strong></h1>
    <p class="line headline-main">Condominiums</p>
    <p class="line headline-date">Delivering Late 2015.</p>

    <div class="rule rule-top"></div>
    <p class="line feature feature-1">· Luxury Finishes</p>
    <p class="line feature feature-2">· Designer Kitchens and Bath</p>
    <p class="line feature feature-3">· Each Unit over 2,000 Square Feet</p>
    <div class="rule rule-bottom"></div>

    <p class="line parking-lead">Deeded Parking</p>
    <p class="line parking-note">Included with Each Unit</p>

    <div class="contact-tag">To Learn More, Contact:</div>
    <p class="line contact contact-names">Marissa Talbot or Vernon Pike</p>
    <p class="line contact contact-phone">(202) 555-0147</p>
    <p class="line contact contact-email">Marissa.Talbot@example-realty.com</p>

    <p class="disclaimer">These Condominium(s) have not been registered by the Office of Residential Standards and Property Oversight Bureau Tenancy Transition and Transfer Section. A Condominium Unit may be reserved on a non-binding reservation agreement, but no contract of sale or lease that is binding on the purchaser may be entered into prior to registration.</p>
  </main>
</body>
</html>
```